Book Cover Design Project - "Cue The Panic"

"Cue the panic - making videos to boost business" is a business book that outlines what you need to know if you are planning to make videos for business communications.
The intended audience for the book is small to medium business owners. These are people who are keen to learn what they should know to do it themselves.
The cover needs to have a clear design that works as a thumbnail as well as full size.
Feel free to have some fun with it. It doesn't have to be all serious. Although this is a business book many people are afraid and don't know where to start with video production.
My company logo uses red, black, grey and white - www.velkarmedia.com.au . The logo has been uploaded.
It is not critical to use those elements, however if it can be incorporated into the design that's good too. The priority however is having a design that is eye catching.
The book will about 200 pages long. The back will include an authors photo, so blurb and testimonials- a word doc has been uploaded. It will also include the barcode, ISBN number, and price.
The spine will need to be clear and eyecatching as well.
The design should clearly reveal that this is about video production and provide a feeling of competency and comfort for those who read it.
Updates

The dimensions for the cover should be 12.8cm x 19.8cm.

At this point the spine thickness will be about 1.5cm x 19.8cm high

Please include my name on the front cover of the design:

Brent Malloway

Target Market(s)

The book is targeted to small to medium business owners who want to know how to make videos for their business. They are do it yourself people.

Industry/Entity Type

Business

Requirements
Must have
• Front
Title: Cue the panic
Tagline: Making videos to boost business

I would also like the spine and back cover done as part of the design, however let's get the front done and then the rest can be completed based on the approved design.
Nice to have
• Cue the panic is a play on words in regards to being filmed (shot) and the anxiety people feel about presenting in front of a camera.
One idea I've had (but I'm not attached to it), is to make the markings that are present in a camera's viewfinder to resemble those that are seen through the sights of a gun.
I'm really not attached to it and unless that can be achieved in a playful way, it is probably best to avoid.
Should not have
• Please avoid images of low budget cameras. The impression we want here is that this is professional standard video production advice. (By the way you don't have to have any cameras at all).

Low budget cameras are handycams etc.

```html
<!DOCTYPE html>
<html lang="en">
<head>
<meta charset="utf-8">
<title>Cue the panic - making videos to boost business</title>
<link rel="stylesheet" href="https://fonts.googleapis.com/css2?family=Anton&family=Cinzel:wght@600&family=Open+Sans:wght@300;600&display=swap">
<style>
  :root {
    --cover-red: #d3202f;
    --title-dark: #3c3c3e;
    --disc-white: #ffffff;
    --bg-centre: #6a6a6a;
    --bg-edge: #161616;
    --hole-grey: #8d8d8d;
    --tagline-white: #ffffff;
  }
  html, body {
    margin: 0;
    padding: 0;
    overflow: hidden;
    background: #ffffff;
  }
  .cover {
    position: relative;
    width: 811px;
    height: 1200px;
    overflow: hidden;
  }
  .cover-art {
    position: absolute;
    inset: 0;
    display: block;
  }
  .title-line {
    font-family: "Anton", "Oswald", sans-serif;
  }
  .title-top { fill: var(--cover-red); }
  .title-bottom { fill: var(--title-dark); }
  .brand-name {
    font-family: "Open Sans", sans-serif;
    font-weight: 600;
    fill: var(--cover-red);
  }
  .tagline {
    font-family: "Cinzel", serif;
    font-weight: 600;
    fill: var(--tagline-white);
  }
  .author-band {
    position: absolute;
    left: 0;
    bottom: 0;
    width: 811px;
    height: 110px;
    background: var(--cover-red);
    display: flex;
    align-items: center;
  }
  .author-name {
    margin: 0 0 0 73px;
    font-family: "Open Sans", sans-serif;
    font-weight: 300;
    font-size: 72px;
    line-height: 1;
    letter-spacing: 7px;
    color: var(--tagline-white);
    white-space: nowrap;
  }
</style>
</head>
<body>
<main class="cover">
  <svg class="cover-art" width="811" height="1200" viewBox="0 0 811 1200" xmlns="http://www.w3.org/2000/svg">
    <defs>
      <radialGradient id="barrel-shade" cx="411" cy="403" r="760" gradientUnits="userSpaceOnUse">
        <stop offset="0" stop-color="var(--bg-centre)"/>
        <stop offset="0.55" stop-color="#3a3a3a"/>
        <stop offset="1" stop-color="var(--bg-edge)"/>
      </radialGradient>
    </defs>

    <rect class="barrel-backdrop" width="811" height="1200" fill="url(#barrel-shade)" role="img" aria-label="Dark grey gun barrel rifling spiral backdrop"/>

    <circle class="bullet-hole" cx="80" cy="107" r="32" fill="var(--hole-grey)" role="img" aria-label="Bullet hole"/>
    <circle class="bullet-hole" cx="767" cy="22" r="32" fill="var(--hole-grey)" role="img" aria-label="Bullet hole"/>
    <circle class="bullet-hole" cx="707" cy="673" r="34" fill="var(--hole-grey)" role="img" aria-label="Bullet hole"/>

    <circle class="title-disc" cx="411" cy="403" r="336" fill="var(--disc-white)"/>

    <text class="title-line title-top" x="131" y="407" font-size="205" textLength="542" lengthAdjust="spacingAndGlyphs">CUE THE</text>
    <text class="title-line title-bottom" x="133" y="571" font-size="151" textLength="420" lengthAdjust="spacingAndGlyphs">PANIC</text>

    <g class="reticle">
      <circle cx="628" cy="505" r="30" fill="var(--title-dark)"/>
      <circle cx="628" cy="505" r="46" fill="none" stroke="var(--title-dark)" stroke-width="3"/>
      <line x1="570" y1="505" x2="692" y2="505" stroke="var(--title-dark)" stroke-width="3"/>
      <line x1="628" y1="438" x2="628" y2="575" stroke="var(--title-dark)" stroke-width="3"/>
    </g>

    <g class="brand">
      <circle cx="263" cy="633" r="22" fill="var(--cover-red)"/>
      <text class="brand-name" x="300" y="647" font-size="38" textLength="253" lengthAdjust="spacingAndGlyphs">VELKAR MEDIA</text>
    </g>

    <g class="tagline-block">
      <text class="tagline" x="405" y="800" font-size="56" text-anchor="middle" textLength="590" lengthAdjust="spacingAndGlyphs">MAKING VIDEOS</text>
      <line x1="97" y1="866" x2="320" y2="866" stroke="var(--tagline-white)" stroke-width="3"/>
      <text class="tagline" x="398" y="884" font-size="56" text-anchor="middle">TO</text>
      <line x1="476" y1="866" x2="700" y2="866" stroke="var(--tagline-white)" stroke-width="3"/>
      <text class="tagline" x="405" y="966" font-size="56" text-anchor="middle" textLength="594" lengthAdjust="spacingAndGlyphs">BOOST BUSINESS</text>
    </g>
  </svg>

  <div class="author-band">
    <p class="author-name">BRENT MALLOWAY</p>
  </div>
</main>
</body>
</html>
```